R. Talbin Group Business Card

We are looking for a business card mock-up.

Contact Information for Business Card

This is the information that needs to be included:
Name
Title
The R. Talbin Group Inc. Insurance Agents & Brokers (needs to be listed out in entirety)
Logo
License 0482316 (needs to be same sized font as phone number)
Address (728 North Vale Avenue, Los Angeles, CA 90047)
Telephone number ( 714-389-2076 ext. 131)Fax number (714-389-4152)
Email
Website (www.rtalbinagency.example)
Cities (Anaheim, Los Angeles, San Jose, Torrance)

```html
<!DOCTYPE html>
<html lang="en">
<head>
<meta charset="utf-8">
<title>R. Talbin Group Business Card</title>
<link href="https://fonts.googleapis.com/css2?family=PT+Serif:wght@400;700&family=Arimo:wght@400&display=swap" rel="stylesheet">
<style>
  :root {
    --backdrop: #d6d6d6;
    --card: #f7f7f6;
    --ink: #1e1a17;
    --ink-soft: #3a3532;
    --copper: #a8642c;
    --copper-line: #c9a27f;
    --faint: #ebebea;
  }
  * { box-sizing: border-box; margin: 0; padding: 0; }
  html, body { width: 1200px; height: 852px; overflow: hidden; }
  body {
    background: var(--backdrop);
    font-family: "PT Serif", Georgia, serif;
    color: var(--ink);
    position: relative;
  }
  .card {
    position: absolute;
    top: 270px;
    width: 520px;
    height: 300px;
    background: var(--card);
    border-radius: 22px;
    overflow: hidden;
    box-shadow: 0 6px 18px rgba(0,0,0,0.18);
  }
  .card-front { left: 50px; }
  .card-back { left: 630px; }

  .faint-circle {
    position: absolute;
    width: 300px; height: 300px;
    border: 22px solid var(--faint);
    border-radius: 50%;
  }
  .card-front .faint-circle { right: -60px; top: -70px; }
  .card-back .faint-circle { right: -90px; top: -60px; }

  .brand-mark {
    width: 54px; height: 54px;
    border-radius: 50%;
    background: var(--copper);
    border: 3px solid var(--ink);
    flex: none;
  }
  .brand-name {
    font-family: "PT Serif", Georgia, serif;
    font-weight: 400;
    color: var(--ink);
    letter-spacing: 1px;
    text-transform: uppercase;
    white-space: nowrap;
  }
  .brand-sub {
    font-family: "PT Serif", Georgia, serif;
    font-size: 8.5px;
    color: var(--ink);
    text-transform: uppercase;
    letter-spacing: 3px;
    white-space: nowrap;
  }

  .front-brand {
    position: absolute;
    left: 50px; top: 108px;
    display: flex; align-items: center; gap: 16px;
  }
  .front-brand .brand-name { font-size: 34px; line-height: 1; }
  .front-brand .brand-sub { margin-top: 6px; letter-spacing: 4.6px; }
  .city-list {
    position: absolute;
    right: 34px; bottom: 30px;
    font-family: "Arimo", Arial, sans-serif;
    font-size: 13px;
    color: var(--ink-soft);
  }
  .city-list .sep { color: var(--copper); margin: 0 5px; }

  .back-brand {
    position: absolute;
    left: 16px; top: 62px;
    width: 228px;
    display: flex; flex-direction: column; align-items: center; gap: 12px;
    text-align: center;
  }
  .back-brand .brand-mark { width: 64px; height: 64px; }
  .back-brand .brand-name { font-size: 23px; line-height: 1; }
  .back-brand .brand-sub { font-size: 7.5px; letter-spacing: 1.6px; line-height: 1.6; margin-top: -6px; }
  .divider {
    position: absolute;
    left: 252px; top: 36px;
    width: 1px; height: 170px;
    background: var(--copper-line);
  }
  .contact {
    position: absolute;
    left: 274px; top: 34px;
    font-size: 12.5px;
    line-height: 1.35;
    color: var(--ink-soft);
  }
  .person-name {
    font-size: 18px;
    color: var(--copper);
    font-variant: small-caps;
    line-height: 1.1;
  }
  .person-title { font-size: 12px; margin-bottom: 12px; }
  .address { margin-bottom: 8px; }
  .contact-row { display: flex; align-items: center; gap: 7px; }
  .contact-row svg { width: 11px; height: 11px; fill: var(--copper); flex: none; }
  .license-tab {
    position: absolute;
    right: 0; bottom: 0;
    width: 250px; height: 48px;
    background: var(--copper);
    border-top-left-radius: 16px;
    color: #fff;
    font-size: 12.5px;
    display: flex; align-items: center; padding-left: 40px;
  }
</style>
</head>
<body>

<section class="card card-front">
  <div class="faint-circle"></div>
  <div class="front-brand">
    <div class="brand-mark"></div>
    <div class="brand-text">
      <p class="brand-name">R. Talbin Group</p>
      <p class="brand-sub">Insurance Agents &amp; Brokers</p>
    </div>
  </div>
  <p class="city-list">Anaheim<span class="sep">|</span>Los Angeles<span class="sep">|</span>San Jose<span class="sep">|</span>Torrance</p>
</section>

<section class="card card-back">
  <div class="faint-circle"></div>
  <div class="back-brand">
    <div class="brand-mark"></div>
    <p class="brand-name">R. Talbin Group</p>
    <p class="brand-sub">The R. Talbin Group Inc.<br>Insurance Agents &amp; Brokers</p>
  </div>
  <div class="divider"></div>
  <div class="contact">
    <p class="person-name">R. Talbin Hale</p>
    <p class="person-title">Managing Director</p>
    <p class="address">728 North Vale Avenue,<br>Los Angeles, CA 90047</p>
    <p class="contact-row">
      <svg viewBox="0 0 12 12" aria-hidden="true"><rect x="1" y="4" width="10" height="7" rx="1.5"/><rect x="0" y="1" width="12" height="3" rx="1.5"/></svg>
      714-389-4152
    </p>
    <p class="contact-row">
      <svg viewBox="0 0 12 12" aria-hidden="true"><path d="M3 1l2 2.5-1.2 1.3a6 6 0 0 0 3.4 3.4L8.5 7 11 9l-1.3 2C5 11 1 7 1 2.3z"/></svg>
      714-389-2076 ext. 131
    </p>
    <p class="contact-row">
      <svg viewBox="0 0 12 12" aria-hidden="true"><path d="M0 2.5h12v7H0z M0 2.5l6 4 6-4" stroke="#fff" stroke-width="0.8"/></svg>
      rtalbin@rtalbinagency.example
    </p>
    <p class="contact-row">
      <svg viewBox="0 0 12 12" aria-hidden="true"><circle cx="6" cy="6" r="5.5"/><path d="M0.5 6h11M6 0.5c-2.5 3-2.5 8 0 11M6 0.5c2.5 3 2.5 8 0 11" stroke="#fff" stroke-width="0.7" fill="none"/></svg>
      www.rtalbinagency.example
    </p>
  </div>
  <div class="license-tab">License 0482316</div>
</section>

</body>
</html>
```